Worksheet for a seminar - wheel of wellbeing

I need a 1 page worksheet for a course I am running next week.
1. The worksheet is based is designed to tie into Valdoric who use 4 colours per specific quadrants - Blue top left, Yellow top right, Green bottom left, Red bottom right. As this is designed to be written and to be printed, it may need to be pale colours however I am open to the correct colours with the image on top if necessary

2. The wellbeing wheel needs to be a design of it's own as it will be used in other things. I would like to have a format for the base wheel that can be changed by me (Only the title names)

3. I have provided the 2 business logo's - these down need to be too big

I hope this helps.

Target Market(s)

Corporate managers and staff - worksheet being used in a workshop

Industry/Entity Type

Wheel

Colors

Designer to choose colors to be used in the design.

Requirements
Must have
• A professional looking wheel that can be used for other purposes. I want to be able to change the 'pie' titles. I will also require a A4 size of the wheel with blank spaces for titles
Nice to have
• A modern feel

```html
<!DOCTYPE html>
<html lang="en">
<head>
<meta charset="utf-8">
<title>Wheel of Wellbeing Worksheet</title>
<link href="https://fonts.googleapis.com/css2?family=Lato:wght@400;700;900&display=swap" rel="stylesheet">
<style>
  :root {
    --page-bg: #d6d6d6;
    --sheet: #ffffff;
    --title-blue: #1e73be;
    --subtitle-red: #e8141c;
    --ink: #2a2a2a;
    --band-grey: #e8e8e8;
    --panel-blue: #4ba3e0;
    --num-red: #ee1c1c;
    --when-grey: #e3e3e3;
    --seg-business: #1b75bb;
    --seg-physical: #4da3e0;
    --seg-emotional: #d9b820;
    --seg-spiritual: #ecd03a;
    --seg-love: #f73c3c;
    --seg-family: #ee1c1c;
    --seg-social: #6aab1d;
    --seg-personal: #84c13a;
    --brand-teal: #3bb89a;
    --brand-green: #5aa832;
  }
  * { box-sizing: border-box; margin: 0; padding: 0; }
  html, body { width: 1200px; height: 1200px; overflow: hidden; background: var(--page-bg); font-family: 'Lato', sans-serif; }
  .sheet {
    position: absolute; left: 192px; top: 30px;
    width: 986px; height: 1380px; background: var(--sheet);
    transform: scale(0.826); transform-origin: 0 0;
  }
  .sheet > * { position: absolute; }
  .title { top: 28px; width: 100%; text-align: center; color: var(--title-blue); font-weight: 900; font-size: 58px; letter-spacing: -0.5px; }
  .subtitle { top: 92px; width: 100%; text-align: center; color: var(--subtitle-red); font-weight: 400; font-size: 44px; }
  .col-label { top: 168px; font-size: 19px; font-weight: 700; color: var(--ink); text-align: center; }
  .col-label.now { left: 0; width: 486px; }
  .col-label.goal { left: 496px; width: 490px; }
  .wheel-band { top: 208px; left: 0; width: 986px; height: 445px; background: var(--band-grey); }
  .wheel-band .divider { position: absolute; left: 478px; top: 35px; width: 4px; height: 380px; background: linear-gradient(90deg, #d0d0d0, #f2f2f2); }
  .wheel { position: absolute; top: 23px; width: 400px; height: 400px; }
  .wheel.now { left: 41px; }
  .wheel.goal { left: 544px; }
  .seg-label { fill: #fff; font-family: 'Lato', sans-serif; font-size: 16px; text-anchor: middle; }
  .date { top: 674px; font-size: 19px; font-weight: 700; color: var(--ink); }
  .date.start { left: 111px; }
  .date.target { left: 572px; }
  .panel { top: 723px; height: 487px; background: var(--panel-blue); }
  .panel.actions { left: 0; width: 493px; }
  .panel.reflect { left: 506px; width: 480px; }
  .panel-head { position: absolute; top: 30px; color: #fff; font-size: 16px; font-weight: 700; }
  .action-row { position: absolute; left: 56px; width: 397px; height: 54px; }
  .action-num { position: absolute; left: 0; top: 0; width: 92px; height: 54px; background: var(--num-red); border-radius: 3px; color: #fff; font-size: 30px; font-weight: 900; display: flex; align-items: center; justify-content: center; }
  .action-bar { position: absolute; left: 92px; top: 2px; width: 305px; height: 52px; background: linear-gradient(90deg, #fff 0 205px, var(--when-grey) 205px); clip-path: polygon(0 0, 91.8% 0, 100% 50%, 91.8% 100%, 0 100%); }
  .question { position: absolute; left: 74px; width: 340px; color: #fff; font-size: 15.5px; font-weight: 700; line-height: 20px; }
  .answer { position: absolute; left: 70px; width: 345px; height: 52px; background: #fff; clip-path: polygon(0 0, 90.4% 0, 100% 50%, 90.4% 100%, 0 100%); }
  .brand { top: 1262px; display: flex; align-items: center; gap: 10px; font-size: 30px; font-weight: 900; }
  .brand.steadfield { left: 196px; color: var(--brand-teal); }
  .brand.brightpath { left: 520px; color: var(--brand-green); }
  .brand .dot { width: 22px; height: 22px; border-radius: 50%; background: var(--brand-teal); }
  .brand .block { width: 22px; height: 22px; background: var(--brand-green); }
  .footer-rule { top: 1370px; left: 0; width: 986px; height: 10px; background: var(--brand-green); }
</style>
</head>
<body>
<div class="sheet">
  <h1 class="title">WHEEL OF WELLBEING</h1>
  <p class="subtitle">a whole brain approach</p>
  <p class="col-label now">Assess where are you now</p>
  <p class="col-label goal">Outcomes Goals &nbsp;where do you want to be?</p>

  <section class="wheel-band">
    <svg class="wheel now" viewBox="-200 -200 400 400" aria-label="Wellbeing wheel, current assessment">
      <defs>
        <path id="segment" d="M77.1,-28 L187.9,-68.4 A200,200 0 0 1 187.9,68.4 L77.1,28 A82,82 0 0 0 77.1,-28 Z"/>
      </defs>
      <g transform="rotate(-127.5)"><use href="#segment" fill="var(--seg-business)"/><text class="seg-label" transform="translate(140,0) rotate(90)"><tspan x="0" y="-14">Business</tspan><tspan x="0" y="4">Career</tspan><tspan x="0" y="22">study</tspan></text></g>
      <g transform="rotate(-82.5)"><use href="#segment" fill="var(--seg-physical)"/><text class="seg-label" transform="translate(140,0) rotate(90)"><tspan x="0" y="-4">Physical</tspan><tspan x="0" y="14">health</tspan></text></g>
      <g transform="rotate(-37.5)"><use href="#segment" fill="var(--seg-emotional)"/><text class="seg-label" transform="translate(140,0) rotate(90)"><tspan x="0" y="-4">Emotional</tspan><tspan x="0" y="14">Health</tspan></text></g>
      <g transform="rotate(7.5)"><use href="#segment" fill="var(--seg-spiritual)"/><text class="seg-label" transform="translate(140,0) rotate(90)"><tspan x="0" y="5">Spritual</tspan></text></g>
      <g transform="rotate(52.5)"><use href="#segment" fill="var(--seg-love)"/><text class="seg-label" transform="translate(140,0) rotate(90)"><tspan x="0" y="-4">Love</tspan><tspan x="0" y="14">Relationship</tspan></text></g>
      <g transform="rotate(97.5)"><use href="#segment" fill="var(--seg-family)"/><text class="seg-label" transform="translate(140,0) rotate(90)"><tspan x="0" y="5">Family</tspan></text></g>
      <g transform="rotate(142.5)"><use href="#segment" fill="var(--seg-social)"/><text class="seg-label" transform="translate(140,0) rotate(90)"><tspan x="0" y="5">Social</tspan></text></g>
      <g transform="rotate(187.5)"><use href="#segment" fill="var(--seg-personal)"/><text class="seg-label" transform="translate(140,0) rotate(90)"><tspan x="0" y="-4">Personal</tspan><tspan x="0" y="14">Growth</tspan></text></g>
    </svg>
    <div class="divider"></div>
    <svg class="wheel goal" viewBox="-200 -200 400 400" aria-label="Wellbeing wheel, goals">
      <g transform="rotate(-127.5)"><use href="#segment" fill="var(--seg-business)"/></g>
      <g transform="rotate(-82.5)"><use href="#segment" fill="var(--seg-physical)"/></g>
      <g transform="rotate(-37.5)"><use href="#segment" fill="var(--seg-emotional)"/></g>
      <g transform="rotate(7.5)"><use href="#segment" fill="var(--seg-spiritual)"/></g>
      <g transform="rotate(52.5)"><use href="#segment" fill="var(--seg-love)"/></g>
      <g transform="rotate(97.5)"><use href="#segment" fill="var(--seg-family)"/></g>
      <g transform="rotate(142.5)"><use href="#segment" fill="var(--seg-social)"/></g>
      <g transform="rotate(187.5)"><use href="#segment" fill="var(--seg-personal)"/></g>
    </svg>
  </section>

  <p class="date start">DATE:</p>
  <p class="date target">DATE ACHIVED BY:</p>

  <section class="panel actions">
    <span class="panel-head" style="left:163px">Action Plan Action</span>
    <span class="panel-head" style="left:368px">When</span>
    <div class="action-row" style="top:72px"><div class="action-num">1</div><div class="action-bar"></div></div>
    <div class="action-row" style="top:178px"><div class="action-num">2</div><div class="action-bar"></div></div>
    <div class="action-row" style="top:286px"><div class="action-num">3</div><div class="action-bar"></div></div>
    <div class="action-row" style="top:390px"><div class="action-num">4</div><div class="action-bar"></div></div>
  </section>

  <section class="panel reflect">
    <p class="question" style="top:26px">Reflect Are they any surprised in your wheel</p>
    <div class="answer" style="top:62px"></div>
    <p class="question" style="top:126px">what wellbeing being gaps stand out as being mood important</p>
    <div class="answer" style="top:175px"></div>
    <p class="question" style="top:245px">How do you feel about it?</p>
    <div class="answer" style="top:289px"></div>
    <p class="question" style="top:361px;left:72px">How might this affect your homelife/worklife</p>
    <div class="answer" style="top:395px"></div>
  </section>

  <div class="brand steadfield"><span class="dot"></span>Steadfield Wellness</div>
  <div class="brand brightpath"><span class="block"></span>Brightpath Ventures</div>
  <div class="footer-rule"></div>
</div>
</body>
</html>
```